Lark Rx discount card
Prescription drug card
We don't need lines for ID numbers.
good job so far. we are looking for rounded corners to make it look like a benefit card not a business card.
I need designs asap. I gave two logos to be used on the Lark Rx Card logo and the Sundial Rx logo which goes on the lower right side smaller than top.
I also gave 5 examples of other cards out there. Look forward to seeing your ideas.

```html
<!DOCTYPE html>
<html lang="en">
<head>
<meta charset="utf-8">
<title>Lark Rx Card – Front and Back</title>
<link href="https://fonts.googleapis.com/css2?family=Cinzel:wght@700&family=Tinos:ital,wght@0,400;0,700;1,400;1,700&display=swap" rel="stylesheet">
<style>
  :root{
    --bg:#e9e6e2;
    --card:#ffffff;
    --card-tint:#e3ecf5;
    --navy:#1f3a78;
    --blue:#2a5fb0;
    --blue-deep:#163f8a;
    --red:#d8262c;
    --grey:#7d8288;
    --line:#9aa3ad;
    --ink:#2b2f36;
  }
  *{box-sizing:border-box;margin:0;padding:0}
  html,body{width:1200px;height:908px;overflow:hidden;background:var(--bg)}
  .canvas{position:relative;width:1200px;height:908px}
  .card{
    position:absolute;width:660px;height:384px;border-radius:22px;overflow:hidden;
    background:linear-gradient(160deg,var(--card) 0%,var(--card) 45%,var(--card-tint) 100%);
    box-shadow:0 10px 24px rgba(0,0,0,.22);
    font-family:"Tinos",serif;color:var(--ink);
  }
  .card--front{left:52px;top:46px}
  .card--back{left:470px;top:470px}
  .wave{position:absolute;left:0;top:0;width:660px;height:384px}
  .brand{position:absolute;left:30px;top:34px;display:flex;align-items:center;gap:14px}
  .brand__dot{width:46px;height:46px;border-radius:50%;background:var(--navy)}
  .brand__name{font-family:"Cinzel",serif;font-weight:700;font-size:40px;color:var(--navy);letter-spacing:1px;line-height:1}
  .tagline{position:absolute;left:32px;top:92px;font-style:italic;font-weight:700;font-size:15px;color:var(--navy)}
  .badge{position:absolute;right:22px;top:22px;width:182px;padding:7px 10px 6px;background:var(--red);color:#fff;text-align:center;border-radius:3px}
  .badge__title{font-weight:700;font-size:23px;line-height:1}
  .badge__sub{font-style:italic;font-size:13px;margin-top:3px}
  .help{position:absolute;right:36px;top:90px;text-align:left;font-size:17px;line-height:1.25}
  .help__label{color:var(--navy)}
  .help__phone{color:var(--red)}
  .partner{position:absolute;right:40px;top:150px;font-size:27px;color:var(--grey);letter-spacing:1px}
  .fields{position:absolute;left:40px;list-style:none;font-size:19px}
  .fields li{display:flex;align-items:flex-end;height:38px}
  .fields .label{width:100px}
  .fields .rule{border-bottom:1px dotted var(--line);height:1px;margin-left:14px}
  .card--front .fields{top:146px}
  .card--back .fields{top:138px}
  .card--back .fields li{height:42px}
  .card--back .label{width:120px}
  .card--back .rule{width:330px}
  .visit{position:absolute;right:58px;bottom:22px;color:#fff;font-size:14px;line-height:1.45;text-align:left}
  .terms{position:absolute;left:22px;top:236px}
  .terms__tab{display:inline-block;background:var(--blue);color:#fff;font-style:italic;font-size:15px;padding:3px 26px 3px 16px;border-radius:0 12px 0 0}
  .terms__list{list-style:none;font-size:13px;margin:6px 0 0 18px;line-height:1.5}
  .terms__list li::before{content:"\2022";margin-right:6px}
</style>
</head>
<body>
<div class="canvas">

  <section class="card card--front" aria-label="Lark Rx Card front">
    <svg class="wave" viewBox="0 0 660 384" aria-hidden="true">
      <defs>
        <linearGradient id="blueFront" x1="0" y1="0" x2="1" y2="1">
          <stop offset="0" stop-color="#3b74c4"/><stop offset="1" stop-color="#163f8a"/>
        </linearGradient>
      </defs>
      <path d="M0,384 L0,362 C220,356 430,330 660,236 L660,384 Z" fill="url(#blueFront)"/>
      <path d="M0,340 C220,334 430,302 660,200 L660,218 C430,318 220,348 0,354 Z" fill="#d8262c"/>
    </svg>
    <div class="brand"><span class="brand__dot"></span><span class="brand__name">Lark Rx Card</span></div>
    <p class="tagline">Your key to prescription drug savings!</p>
    <div class="badge"><div class="badge__title">FREE Benefits</div><div class="badge__sub">Prescription Saving Card</div></div>
    <div class="help"><div class="help__label">NEED HELP</div><div class="help__phone">Call: 1-800-555-0142</div></div>
    <div class="partner">SUNDIAL Rx</div>
    <ul class="fields">
      <li><span class="label">Member Id</span>:</li>
      <li><span class="label">Group Id</span>:</li>
      <li><span class="label">Bin</span>:</li>
      <li><span class="label">Pcn</span>:</li>
    </ul>
    <p class="visit">for more information please visit:<br>WWW.LARKRX.COM</p>
  </section>

  <section class="card card--back" aria-label="Lark Rx Card back">
    <svg class="wave" viewBox="0 0 660 384" aria-hidden="true">
      <defs>
        <linearGradient id="blueBack" x1="0" y1="0" x2="1" y2="1">
          <stop offset="0" stop-color="#3b74c4"/><stop offset="1" stop-color="#163f8a"/>
        </linearGradient>
      </defs>
      <path d="M0,384 L0,366 C220,360 430,336 660,246 L660,384 Z" fill="url(#blueBack)"/>
      <path d="M0,346 C220,340 430,310 660,212 L660,230 C430,326 220,354 0,360 Z" fill="#d8262c"/>
    </svg>
    <div class="brand"><span class="brand__dot"></span><span class="brand__name">Lark Rx Card</span></div>
    <p class="tagline">Your key to prescription drug savings!</p>
    <div class="badge"><div class="badge__title">FREE Benefits</div><div class="badge__sub">Prescription Saving Card</div></div>
    <div class="help"><div class="help__label">NEED HELP</div><div class="help__phone">Call: 1-800-555-0142</div></div>
    <div class="partner">SUNDIAL Rx</div>
    <ul class="fields">
      <li><span class="label">Patient</span>:<span class="rule"></span></li>
      <li><span class="label">Pharmacist</span>:<span class="rule"></span></li>
    </ul>
    <div class="terms">
      <span class="terms__tab">Terms &amp; Condition</span>
      <ul class="terms__list">
        <li>This is not insurance</li>
        <li>This card does not expire</li>
      </ul>
    </div>
    <p class="visit">for more information please visit:<br>WWW.LARKRX.COM</p>
  </section>

</div>
</body>
</html>
```